Kitesurf Weather Forecast Application Needs an Advertising Banner

We need an Advertising Banner for our iOS Kitesurf Weather Forecast Application. The application name is GustMapper and you can download it from the Plum Depot.

https://apps.plumdepot-market.com/app/gustmapper-breeze-and-sky-outlook/id804417392?mt=8

The banner should have the logo of our application, which can be either found from the Plum Depot or uploaded on this post. It should describe what our app does with either words or graphic story. GustMapper is a weather forecast application for Kitesurfers. As the banner is small, animated gifs will also be considered.

We need the following sizes 320x50 and 728x90. The banner will be uploaded to tavlo. Tavlo accepts images in PNG, JPEG and GIF. We want it in one of the formats that can be uploaded to TavLo and vector .ai so we can make changed if necessary in the future.

On tap the banner will open Plum Depot on the user's device and present GustMapper.

06/09. I added a screenshot from an application that the banner will be added. The screenshot is from an Lumafon 4 Max (it is from a big device). The red area on the bottom is where the advert will go and it should be readable.

Target Market(s)

Banner will be displayed in other iOS Applications. One of them is Rigging Reckoner https://apps.plumdepot-market.com/us/app/rigging-reckoner/id937206148?mt=8

Industry/Entity Type

Advertising

Font styles to use
Other font styles liked:
• San Francisco

Requirements
Must have
• GustMapper logo and communicate a clear message on what the application does. GustMapper is a weather forecast application for Kitesurfers. If you want to find more information please visit the PlumDepot link provided.
Nice to have
• Animated gif will be nice to have, as the banner is small and it maybe difficult to communicate the message required.
Should not have
• We prefer something minimal and along the lines of our application design.

```html
<!DOCTYPE html>
<html lang="en">
<head>
<meta charset="utf-8">
<title>GustMapper Banner Set</title>
<link href="https://fonts.googleapis.com/css2?family=Inter:wght@400&family=Lora:ital,wght@1,400&family=Poppins:wght@400;500;600&display=swap" rel="stylesheet">
<style>
  :root {
    --canvas: #ffffff;
    --panel-dark: #333436;
    --brand-orange: #ff8a00;
    --cta-yellow: #eeff00;
    --cta-text: #2a2a2a;
    --text-light: #ffffff;
    --label-ink: #111111;
    --sky-top: #3b9bee;
    --sky-mid: #7fbdf2;
    --sky-low: #cfe5f7;
    --icon-tile: #a9b7a8;
    --icon-edge: #d8dfd6;
  }
  * { margin: 0; padding: 0; box-sizing: border-box; }
  html, body {
    width: 1200px; height: 816px; overflow: hidden;
    background: var(--canvas);
  }
  .stage {
    position: relative;
    width: 850px; height: 578px;
    transform: scale(1.41176);
    transform-origin: 0 0;
  }
  .size-label {
    position: absolute;
    font-family: "Inter", sans-serif;
    font-weight: 400;
    font-size: 30px;
    letter-spacing: 0.5px;
    color: var(--label-ink);
    line-height: 1;
  }
  .size-label--leader { left: 265px; top: 24px; }
  .size-label--mobile { left: 240px; top: 478px; }

  .banner {
    position: absolute;
    display: flex;
    overflow: hidden;
  }
  .banner__brand {
    position: relative;
    background: var(--panel-dark);
    height: 100%;
  }
  .banner__sky {
    position: relative;
    flex: 1;
    height: 100%;
    background: linear-gradient(170deg, var(--sky-top) 0%, var(--sky-mid) 55%, var(--sky-low) 100%);
    display: flex; align-items: center; justify-content: center;
    text-align: center;
    color: var(--text-light);
    font-family: "Poppins", sans-serif;
  }
  .app-tile {
    position: absolute;
    background: linear-gradient(160deg, var(--icon-edge), var(--icon-tile));
  }
  .app-name {
    position: absolute;
    font-family: "Poppins", sans-serif;
    font-weight: 600;
    color: var(--brand-orange);
    line-height: 1;
    white-space: nowrap;
  }
  .cta {
    position: absolute;
    background: var(--cta-yellow);
    color: var(--cta-text);
    font-family: "Poppins", sans-serif;
    font-weight: 500;
    display: flex; align-items: center; justify-content: center;
    border-radius: 999px;
  }

  /* 728 x 90 */
  .banner--leader { left: 81px; width: 728px; height: 90px; }
  .banner--leader .banner__brand { width: 405px; }
  .banner--leader .app-tile { left: 8px; top: 14px; width: 62px; height: 62px; border-radius: 10px; }
  .banner--leader .app-name { left: 84px; top: 15px; font-size: 25px; }
  .banner--leader .tagline {
    position: absolute; left: 86px; top: 43px;
    font-family: "Lora", serif; font-style: italic;
    font-size: 15.5px; line-height: 19px;
    color: var(--text-light);
  }
  .banner--leader .cta { left: 269px; top: 28px; width: 110px; height: 35px; font-size: 14px; }
  .banner--leader .banner__sky {
    font-weight: 600; font-size: 18.5px; line-height: 25px;
    text-transform: uppercase;
    text-shadow: 0 1px 3px rgba(0, 40, 90, 0.45);
  }

  /* 320 x 50 */
  .banner--mobile { left: 481px; width: 320px; height: 50px; }
  .banner--mobile .banner__brand { width: 160px; }
  .banner--mobile .app-tile { left: 7px; top: 4px; width: 43px; height: 43px; border-radius: 7px; }
  .banner--mobile .app-name { left: 55px; top: 4px; font-size: 15.5px; }
  .banner--mobile .cta { left: 63px; top: 24px; width: 80px; height: 20px; font-size: 10px; }
  .banner--mobile .banner__sky { font-weight: 400; font-size: 12px; line-height: 15px; }
</style>
</head>
<body>
<main class="stage">
  <div class="size-label size-label--leader">728X90</div>

  <section class="banner banner--leader" style="top:67px">
    <div class="banner__brand">
      <div class="app-tile" role="img" aria-label="App icon tile"></div>
      <div class="app-name">GustMapper</div>
      <p class="tagline">Kitesurf wind and<br>weather forecast</p>
      <div class="cta">Click Here</div>
    </div>
    <div class="banner__sky" role="img" aria-label="Blue sky with soft clouds">
      <p>Weekly forecast showing<br>only kitable spots</p>
    </div>
  </section>

  <section class="banner banner--leader" style="top:169px">
    <div class="banner__brand">
      <div class="app-tile" role="img" aria-label="App icon tile"></div>
      <div class="app-name">GustMapper</div>
      <p class="tagline">Kitesurf wind and<br>weather forecast</p>
      <div class="cta">Click Here</div>
    </div>
    <div class="banner__sky" role="img" aria-label="Blue sky with soft clouds">
      <p>Live weather checkout<br>live stations</p>
    </div>
  </section>

  <section class="banner banner--leader" style="top:269px">
    <div class="banner__brand">
      <div class="app-tile" role="img" aria-label="App icon tile"></div>
      <div class="app-name">GustMapper</div>
      <p class="tagline">Kitesurf wind and<br>weather forecast</p>
      <div class="cta">Click Here</div>
    </div>
    <div class="banner__sky" role="img" aria-label="Blue sky with soft clouds">
      <p>Detailed weather see<br>hourly forecast &amp; live</p>
    </div>
  </section>

  <div class="size-label size-label--mobile">320X50</div>

  <section class="banner banner--mobile" style="top:388px">
    <div class="banner__brand">
      <div class="app-tile" role="img" aria-label="App icon tile"></div>
      <div class="app-name">GustMapper</div>
      <div class="cta">Click Here</div>
    </div>
    <div class="banner__sky" role="img" aria-label="Blue sky with soft clouds">
      <p>Detailed weather see<br>hourly forecast &amp; live</p>
    </div>
  </section>

  <section class="banner banner--mobile" style="top:448px">
    <div class="banner__brand">
      <div class="app-tile" role="img" aria-label="App icon tile"></div>
      <div class="app-name">GustMapper</div>
      <div class="cta">Click Here</div>
    </div>
    <div class="banner__sky" role="img" aria-label="Blue sky with soft clouds">
      <p>Live weather Checkout<br>live stations</p>
    </div>
  </section>

  <section class="banner banner--mobile" style="top:506px">
    <div class="banner__brand">
      <div class="app-tile" role="img" aria-label="App icon tile"></div>
      <div class="app-name">GustMapper</div>
      <div class="cta">Click Here</div>
    </div>
    <div class="banner__sky" role="img" aria-label="Blue sky with soft clouds">
      <p>Detailed weather see<br>hourly forecast &amp; live</p>
    </div>
  </section>
</main>
</body>
</html>
```